Interior Design & Furniture E commerce Website Design

I need a cutting edge website design, this is for Interior Design Services as well as eCommerce for furniture and home decor www.lorivellstudio.com
Here is a sample of the concept behind the site.
I am a furniture & Interior Designer, want to create a life style brand.
Will offer Interior Design Services : Commercial & Residential (this portion will be a catalog or portfolio type)
The eCommerce side will sell, Furniture, Lighting, Decor, Gifts, Textiles, will also be offering trade so that could be at bottom of site. I also like the concept of concierge as where all the info falls under: shipping, etc..

*Please make sure to make the eCommerce prominent.

Hello Designers, I also would like to possibly update my logo, the current one I like but don't Love.

Target Market(s)

High end customers with disposable income, who also appreciate quality and unique furniture & design

Number of Pages Required

5+ page

Colors
0255a3
f37122

Requirements
Must have
• Room Planer: I will be using this tool http://kvstudio.tarnebworks.com/room-planner.inc
• Live Chat
• Will be offering 3d renderings for spaces as well as Virtual Reality
• The image I loaded that looks like copper, I would like to have that as a color on the site with the texture: so the colors are Blue and copper. Would like the site to be user friendly and interactive
• http://kvstudio.tarnebworks.com/ (this is the current site in development, so we will be offering Design your own, Trends, inspiration, etc...
• I have included a headshot to use for now about me. or about us.
• I also included several actual project installation (residential and commercial) as well as a variety of my furniture items
• I have Included an old Bio and some articles I would like to show case in a Press Area
• I would also like to include a section for Events (Giving back )I do a lot of charity events 1-2 a year and would like to showcase that as well
• *Please make the store (ecommerce prominent )

```html
<!DOCTYPE html>
<html lang="en">
<head>
<meta charset="utf-8">
<title>Lori Vell Design</title>
<link href="https://fonts.googleapis.com/css2?family=Raleway:wght@400;600;700;800&family=Open+Sans:wght@400;600;700&display=swap" rel="stylesheet">
<style>
:root{
  --navy:#1f3a5e;
  --navy-deep:#172c48;
  --copper:#a9602c;
  --copper-light:#c47a3f;
  --ink:#2a2a2a;
  --muted:#7a7a7a;
  --line:#e3e3e3;
  --paper:#ffffff;
  --soft:#f7f7f7;
}
*{box-sizing:border-box;margin:0;padding:0}
html,body{width:1200px;height:5172px;overflow:hidden}
body{font-family:"Open Sans",Arial,sans-serif;color:var(--ink);background:var(--paper);font-size:14px}
h1,h2,h3,h4,.display{font-family:"Raleway",Arial,sans-serif}
.wrap{width:1056px;margin:0 auto}
svg{display:block}

.topbar{height:32px;background:var(--navy);color:#fff;font-size:12px}
.topbar .wrap{display:flex;justify-content:space-between;align-items:center;height:100%}
.topbar .group{display:flex;gap:22px;align-items:center}
.topbar .item{display:flex;gap:6px;align-items:center}

.header{height:120px;background:var(--paper);border-bottom:1px solid var(--line)}
.header .wrap{display:flex;align-items:center;justify-content:space-between;height:100%}
.nav{display:flex;gap:26px;font-size:14px;font-weight:600;color:var(--navy);align-items:center}
.brand{display:flex;align-items:center;gap:10px}
.brand-mark{width:14px;height:14px;background:var(--copper)}
.brand-name{font-family:"Raleway",sans-serif;font-weight:700;font-size:24px;letter-spacing:3px;color:var(--navy)}

.hero{height:488px;position:relative;color:#fff;text-align:center;display:flex;flex-direction:column;align-items:center;justify-content:center;
  background:
    linear-gradient(180deg,rgba(20,20,20,.15),rgba(20,20,20,.35)),
    radial-gradient(ellipse at 22% 70%,#9a3a2c 0%,rgba(154,58,44,0) 38%),
    radial-gradient(ellipse at 78% 72%,#8c2f26 0%,rgba(140,47,38,0) 36%),
    radial-gradient(ellipse at 12% 20%,#7f9fb8 0%,rgba(127,159,184,0) 30%),
    linear-gradient(100deg,#4e5a48 0%,#7a6650 30%,#a08868 52%,#6a5848 72%,#2e2824 100%)}
.hero h1{font-size:60px;font-weight:600;letter-spacing:1px;text-shadow:0 2px 8px rgba(0,0,0,.45)}
.hero p{font-size:24px;margin-top:10px;max-width:540px;line-height:1.35;text-shadow:0 1px 4px rgba(0,0,0,.4)}

.newsletter{height:100px;display:flex}
.newsletter .signup{flex:0 0 780px;background:var(--navy);color:#fff;display:flex;align-items:center;justify-content:space-between;padding:0 60px 0 72px}
.signup h3{font-size:26px;font-weight:700}
.signup p{font-size:11px;color:#c9d3e0;margin-top:6px}
.newsletter .projects{flex:1;background:linear-gradient(120deg,#9a5325,#b86d34 50%,#94501f);color:#fff;display:flex;align-items:center;justify-content:center;font-family:"Raleway",sans-serif;font-size:28px;font-weight:700;letter-spacing:1px}

.welcome{height:320px;text-align:center;padding-top:44px}
.section-title{font-size:40px;font-weight:700;color:var(--navy);text-transform:uppercase}
.rule{width:80px;height:3px;background:var(--copper);margin:12px auto 0}
.welcome p{width:880px;margin:20px auto 0;font-size:13px;line-height:1.8;color:var(--muted)}
.round-btn{width:56px;height:56px;border:2px solid var(--navy);border-radius:50%;margin:22px auto 0;display:flex;align-items:center;justify-content:center}

.services{height:312px;display:flex}
.service{flex:1;position:relative}
.service .label{position:absolute;left:0;right:0;bottom:0;height:52px;background:rgba(23,44,72,.88);color:#fff;font-family:"Raleway",sans-serif;font-weight:700;font-size:18px;display:flex;align-items:center;padding-left:28px}
.service.featured .label{background:var(--copper)}
.s1{background:
  radial-gradient(circle at 30% 25%,#f0b060 0%,rgba(240,176,96,0) 14%),
  radial-gradient(circle at 70% 20%,#f3c070 0%,rgba(243,192,112,0) 12%),
  radial-gradient(ellipse at 50% 80%,#c23a2a 0%,rgba(194,58,42,0) 50%),
  linear-gradient(160deg,#3a1210,#8a2a22 45%,#5a1a16 75%,#2a0e0c)}
.s2{background:
  radial-gradient(ellipse at 40% 30%,#d8d0c8 0%,rgba(216,208,200,0) 20%),
  radial-gradient(ellipse at 60% 75%,#9a2a30 0%,rgba(154,42,48,0) 40%),
  linear-gradient(150deg,#1e1e26,#4a3a44 45%,#2a2430 80%,#16161c)}
.s3{background:
  radial-gradient(ellipse at 60% 80%,#4fa2c4 0%,rgba(79,162,196,0) 40%),
  linear-gradient(180deg,#b8d4ea 0%,#e0d4bc 45%,#a88a68 62%,#5e9cb8 80%,#7a6a58 100%)}

.about{height:588px}
.about .wrap{display:flex;gap:70px;align-items:center;height:100%;padding-left:60px}
.portrait{width:320px;height:320px;border-radius:50%;flex:0 0 auto;
  background:radial-gradient(circle at 50% 40%,#f2f2f2 0%,#c8c8c8 45%,#6a6a6a 100%)}
.about h2{font-size:40px;font-weight:700;color:var(--copper)}
.about p{font-size:13px;line-height:1.85;color:var(--muted);margin-top:18px}
.btn{display:inline-block;background:var(--navy);color:#fff;font-family:"Raleway",sans-serif;font-weight:700;font-size:15px;padding:14px 28px;text-transform:uppercase}
.about .btn{margin-top:24px}

.testimonial{height:440px;position:relative;color:#fff;text-align:center;padding-top:60px;
  background:
    linear-gradient(rgba(28,40,64,.78),rgba(28,40,64,.78)),
    radial-gradient(ellipse at 20% 40%,#8a6a50 0%,rgba(138,106,80,0) 40%),
    radial-gradient(ellipse at 80% 50%,#6a5a70 0%,rgba(106,90,112,0) 40%),
    linear-gradient(135deg,#3a3a48,#6a5a58 50%,#2a2a3a)}
.testimonial h2{font-size:40px;font-weight:700}
.avatar{width:90px;height:90px;border-radius:50%;background:radial-gradient(circle at 50% 40%,#f0d8c0,#a07a60);border:3px solid #fff;margin:28px auto 0}
.testimonial blockquote{width:640px;margin:22px auto 0;font-size:13px;line-height:1.75;color:#dfe5ee}
.testimonial .who{margin-top:20px;font-family:"Raleway",sans-serif;font-weight:700;font-size:14px;display:flex;gap:10px;align-items:center;justify-content:center}
.testimonial .who::before{content:"";width:26px;height:2px;background:var(--copper-light)}
.side-arrow{position:absolute;top:50%;width:40px;height:40px;border-radius:50%;background:rgba(255,255,255,.2);display:flex;align-items:center;justify-content:center;transform:translateY(-50%)}
.side-arrow.left{left:20px}
.side-arrow.right{right:20px}

.trends{height:1160px;padding-top:70px;text-align:center}
.tabs{display:flex;gap:14px;justify-content:center;margin-top:30px}
.tab{border:1px solid var(--navy);color:var(--navy);font-size:14px;padding:7px 28px;border-radius:4px}
.tab.active{background:var(--navy);color:#fff}
.grid{display:grid;grid-template-columns:repeat(4,252px);gap:36px 16px;margin-top:40px;text-align:center}
.card{border:1px solid var(--line);position:relative;overflow:hidden;background:#fff}
.card .photo{height:230px;padding:14px;background:#fff}
.card .photo div{width:100%;height:100%}
.card h4{font-size:15px;font-weight:700;margin-top:12px;text-transform:uppercase}
.card p{font-size:12px;color:var(--muted);margin:8px 40px 0;line-height:1.5}
.card .buy{display:flex;margin-top:18px;height:40px}
.card .add{flex:1;background:var(--navy);color:#fff;font-size:12px;font-weight:700;display:flex;align-items:center;justify-content:center;gap:8px}
.card .price{width:84px;background:var(--copper);color:#fff;font-weight:700;display:flex;align-items:center;justify-content:center}
.ribbon{position:absolute;top:0;left:0;width:0;height:0;border-top:56px solid var(--navy);border-right:56px solid transparent;z-index:2}
.ribbon span{position:absolute;top:-46px;left:4px;color:#fff;font-size:10px;font-weight:700;transform:rotate(-45deg)}
.p1{background:radial-gradient(ellipse at 50% 45%,#a8a49a 0%,#d8d4cc 45%,#fafafa 75%)}
.p2{background:radial-gradient(ellipse at 50% 45%,#b0302a 0%,#6a2a22 35%,#e8dcd8 60%,#fafafa 78%)}
.p3{background:radial-gradient(ellipse at 50% 50%,#5a4a3a 0%,#3a3028 35%,#d8d0c8 62%,#fafafa 80%)}
.p4{background:radial-gradient(ellipse at 50% 45%,#d8b880 0%,#9a7448 38%,#e8dcc8 62%,#fafafa 80%)}
.p5{background:radial-gradient(ellipse at 50% 45%,#7a5a3a 0%,#3a2818 32%,#ddd2c6 58%,#fafafa 78%)}
.p6{background:radial-gradient(ellipse at 50% 55%,#3a7ad0 0%,#1b4a96 30%,#d4e0f0 60%,#fafafa 80%)}
.p7{background:radial-gradient(ellipse at 50% 50%,#c4a878 0%,#7a6040 35%,#e4dccc 62%,#fafafa 80%)}
.p8{background:radial-gradient(ellipse at 50% 55%,#3a4a88 0%,#1c2450 35%,#d4d8e6 62%,#fafafa 80%)}
.trends .btn{margin-top:44px}

.articles{height:460px;position:relative;color:#fff;
  background:
    linear-gradient(90deg,rgba(110,60,25,.35),rgba(110,60,25,.1)),
    radial-gradient(ellipse at 70% 30%,#d89a5a 0%,rgba(216,154,90,0) 45%),
    linear-gradient(100deg,#6e3a18,#a86a34 35%,#c48448 55%,#8a5226 80%,#5e3214)}
.articles .wrap{display:flex;align-items:center;gap:60px;height:100%;padding-left:60px}
.cover{width:300px;height:380px;flex:0 0 auto;
  background:
    radial-gradient(ellipse at 50% 55%,#d86ab0 0%,rgba(216,106,176,0) 40%),
    linear-gradient(175deg,#f4f2f6 0%,#f4f2f6 14%,#8a6ac8 40%,#5a3a9a 75%,#2e2050)}
.articles h2{font-size:40px;font-weight:700}
.articles p{font-size:13px;line-height:1.8;margin-top:18px;max-width:480px;color:#fbe9da}
.articles .btn{margin-top:26px}

.news{height:760px;padding-top:56px;text-align:center}
.news-body{display:flex;gap:20px;margin-top:40px;text-align:left}
.feature{width:668px;border:1px solid var(--line)}
.feature .photo{height:340px;background:
  radial-gradient(ellipse at 30% 60%,#3a8a8a 0%,rgba(58,138,138,0) 35%),
  radial-gradient(ellipse at 75% 40%,#b08a6a 0%,rgba(176,138,106,0) 40%),
  linear-gradient(135deg,#d8cfc0,#9aa49a 45%,#6a7a7a 75%,#4a5458)}
.feature .body{padding:22px 24px}
.feature h4{font-family:"Open Sans",sans-serif;font-size:14px;font-weight:700;color:var(--navy);line-height:1.5}
.meta{display:flex;gap:18px;font-size:12px;color:var(--copper);margin-top:10px}
.meta span{display:flex;gap:6px;align-items:center}
.feature p{font-size:12px;color:var(--muted);line-height:1.7;margin-top:12px}
.feature .foot{display:flex;justify-content:flex-end;margin-top:14px}
.list{flex:1;display:flex;flex-direction:column;gap:22px}
.list-item{display:flex;gap:16px}
.thumb{width:140px;height:112px;flex:0 0 auto}
.list-item h4{font-family:"Open Sans",sans-serif;font-size:15px;font-weight:700;line-height:1.4}
.t1{background:linear-gradient(135deg,#d4b890,#8a5a36 55%,#4a2e1c)}
.t2{background:linear-gradient(135deg,#eee8de,#b8a894 55%,#7c6c5a)}
.t3{background:linear-gradient(135deg,#c8d0d6,#7d8b94 55%,#4a5660)}
.t4{background:linear-gradient(135deg,#e6d4b6,#a8865c 55%,#5e4630)}

.footer{height:320px;background:var(--navy);color:#dbe3ee}
.footer .wrap{display:grid;grid-template-columns:260px 1fr 1fr 1fr;gap:40px;padding-top:52px}
.footer .brand-name{color:#fff;font-size:22px}
.footer .about-text{font-size:12px;line-height:1.7;margin-top:18px}
.footer h5{font-family:"Raleway",sans-serif;font-size:15px;font-weight:700;color:#fff;text-transform:uppercase;margin-bottom:16px}
.footer ul{list-style:none;font-size:12px;line-height:2}
.footer li{display:flex;gap:8px;align-items:center}
.dot{width:14px;height:14px;border-radius:50%;background:var(--copper-light);flex:0 0 auto}
.copyright{height:52px;background:var(--navy-deep);color:#c9d3e0;font-size:12px;display:flex;align-items:center;justify-content:center}
</style>
</head>
<body>

<div class="topbar">
  <div class="wrap">
    <div class="group">
      <span class="item"><svg width="12" height="12" viewBox="0 0 24 24" fill="#fff"><path d="M6.6 10.8a15.1 15.1 0 0 0 6.6 6.6l2.2-2.2a1 1 0 0 1 1-.25 11.4 11.4 0 0 0 3.6.57 1 1 0 0 1 1 1V20a1 1 0 0 1-1 1A17 17 0 0 1 3 4a1 1 0 0 1 1-1h3.5a1 1 0 0 1 1 1c0 1.25.2 2.45.57 3.57a1 1 0 0 1-.25 1z"/></svg>040-555-0148</span>
      <span class="item">Contact Us</span>
    </div>
    <div class="group">
      <span class="item">My Account</span>
      <span class="item">Not Registered?</span>
      <span class="item">Sign in</span>
    </div>
  </div>
</div>

<header class="header">
  <div class="wrap">
    <nav class="nav"><span>Living Room</span><span>Dining Room</span><span>Bedroom</span><span>Home Office</span></nav>
    <div class="brand"><span class="brand-mark"></span><span class="brand-name">LORI VELL</span></div>
    <nav class="nav"><span>Entertainment</span><span>Bathroom</span><span>Accessories</span>
      <svg width="16" height="16" viewBox="0 0 24 24" fill="none" stroke="#1f3a5e" stroke-width="2.5"><circle cx="10" cy="10" r="7"/><path d="M15 15l6 6"/></svg></nav>
  </div>
</header>

<section class="hero" role="img" aria-label="Photo of a furnished outdoor terrace with patterned red armchairs">
  <h1>LORI VELL DESIGN</h1>
  <p>I am a furniture &amp; Interior Designer, want to create a life style brand.</p>
</section>

<section class="newsletter">
  <div class="signup">
    <div>
      <h3>Sign Up For Newsletter</h3>
      <p>Would you like to receive exclusive access to articles, trends and our regular monthly updates?</p>
    </div>
    <svg width="34" height="34" viewBox="0 0 24 24" fill="#fff"><path d="M2 21l21-9L2 3v7l15 2-15 2z"/></svg>
  </div>
  <div class="projects">VIEW PROJECTS</div>
</section>

<section class="welcome">
  <h2 class="section-title">Welcome to Lori Vell</h2>
  <div class="rule"></div>
  <p>As a child, Lori Vell spent long weekends in her father's workshop helping him shape his furniture pieces. She was delighted to be taken along to project installations and see finished rooms come alive. What began as a fun after school hobby grew into a passion for quality craftsmanship and unique furniture and interior design for every space.</p>
  <div class="round-btn"><svg width="20" height="20" viewBox="0 0 24 24" fill="none" stroke="#1f3a5e" stroke-width="3"><path d="M5 15l7-7 7 7"/></svg></div>
</section>

<section class="services">
  <div class="service s1" role="img" aria-label="Photo of a red-toned lounge interior with warm pendant lights"><div class="label">INTERIOR DESIGNER</div></div>
  <div class="service s2 featured" role="img" aria-label="Photo of a furniture showroom"><div class="label">FURNITURE DESIGNER</div></div>
  <div class="service s3" role="img" aria-label="Photo of a residential pool terrace"><div class="label">COMMERCIAL &amp; RESIDENTIAL</div></div>
</section>

<section class="about">
  <div class="wrap">
    <div class="portrait" role="img" aria-label="Headshot of the designer"></div>
    <div>
      <h2>LORI VELL</h2>
      <p>As a child, Lori Vell spent weekends with her father helping in his furniture workshop. She was delighted to be taken along on project installations and loved seeing each piece find its place. What began as a fun after school hobby evolved into a passion for quality craftsmanship and unique furniture. By the age of sixteen she was ready to take the family studio forward, and today her studio creates furniture and interiors for the hospitality and residential trade.</p>
      <a class="btn">Learn More</a>
    </div>
  </div>
</section>

<section class="testimonial">
  <h2>WHAT OUR CLIENT SAY ABOUT US</h2>
  <div class="avatar" role="img" aria-label="Client portrait"></div>
  <blockquote>Working with the studio was a wonderful experience from the first sketch to the final install. Every piece was crafted with care, the rooms feel warm and personal, and the whole team listened closely to what our family really needed in our home.</blockquote>
  <div class="who">CLIENT NAME</div>
  <div class="side-arrow left"><svg width="14" height="14" viewBox="0 0 24 24" fill="none" stroke="#fff" stroke-width="3"><path d="M15 5l-7 7 7 7"/></svg></div>
  <div class="side-arrow right"><svg width="14" height="14" viewBox="0 0 24 24" fill="none" stroke="#fff" stroke-width="3"><path d="M9 5l7 7-7 7"/></svg></div>
</section>

<section class="trends">
  <h2 class="section-title">Our Trands</h2>
  <div class="rule"></div>
  <div class="tabs"><span class="tab active">All</span><span class="tab">Furniture</span><span class="tab">Lighting</span><span class="tab">Decor</span><span class="tab">Gifts</span><span class="tab">Textiles</span></div>
  <div class="wrap grid">
    <div class="card"><div class="ribbon"><span>NEW</span></div><div class="photo"><div class="p1" role="img" aria-label="Grey upholstered armchair"></div></div><h4>Product Name</h4><p>Short product note for this item</p><div class="buy"><span class="add">ADD TO CART</span><span class="price">$55.00</span></div></div>
    <div class="card"><div class="photo"><div class="p2" role="img" aria-label="Red lacquer chair"></div></div><h4>Product Name</h4><p>Short product note for this item</p><div class="buy"><span class="add">ADD TO CART</span><span class="price">$55.00</span></div></div>
    <div class="card"><div class="photo"><div class="p3" role="img" aria-label="Nesting side tables"></div></div><h4>Product Name</h4><p>Short product note for this item</p><div class="buy"><span class="add">ADD TO CART</span><span class="price">$55.00</span></div></div>
    <div class="card"><div class="photo"><div class="p4" role="img" aria-label="Carved cabinet"></div></div><h4>Product Name</h4><p>Short product note for this item</p><div class="buy"><span class="add">ADD TO CART</span><span class="price">$55.00</span></div></div>
    <div class="card"><div class="photo"><div class="p5" role="img" aria-label="Wooden dining chair"></div></div><h4>Product Name</h4><p>Short product note for this item</p><div class="buy"><span class="add">ADD TO CART</span><span class="price">$55.00</span></div></div>
    <div class="card"><div class="photo"><div class="p6" role="img" aria-label="Blue chaise longue"></div></div><h4>Product Name</h4><p>Short product note for this item</p><div class="buy"><span class="add">ADD TO CART</span><span class="price">$55.00</span></div></div>
    <div class="card"><div class="photo"><div class="p7" role="img" aria-label="Pair of brass stools"></div></div><h4>Product Name</h4><p>Short product note for this item</p><div class="buy"><span class="add">ADD TO CART</span><span class="price">$55.00</span></div></div>
    <div class="card"><div class="photo"><div class="p8" role="img" aria-label="Navy sofa"></div></div><h4>Product Name</h4><p>Short product note for this item</p><div class="buy"><span class="add">ADD TO CART</span><span class="price">$55.00</span></div></div>
  </div>
  <a class="btn">View More</a>
</section>

<section class="articles" aria-label="Latest articles">
  <div class="wrap">
    <div class="cover" role="img" aria-label="Magazine cover featuring the designer"></div>
    <div>
      <h2>LATEST ARTICLES</h2>
      <p>Read the latest press features on the studio, from design magazine interviews to behind the scenes stories of recent residential and hospitality projects across the country.</p>
      <a class="btn">Learn More</a>
    </div>
  </div>
  <div class="side-arrow left" style="border-radius:0;background:var(--navy)"><svg width="14" height="14" viewBox="0 0 24 24" fill="none" stroke="#fff" stroke-width="3"><path d="M15 5l-7 7 7 7"/></svg></div>
  <div class="side-arrow right" style="border-radius:0;background:var(--navy)"><svg width="14" height="14" viewBox="0 0 24 24" fill="none" stroke="#fff" stroke-width="3"><path d="M9 5l7 7-7 7"/></svg></div>
</section>

<section class="news">
  <h2 class="section-title">Latest News &amp; Events</h2>
  <div class="rule"></div>
  <div class="wrap news-body">
    <article class="feature">
      <div class="photo" role="img" aria-label="Photo of a design mood board with fabric and material samples"></div>
      <div class="body">
        <h4>Our annual giving back evening raised funds for local family shelters this spring.</h4>
        <div class="meta"><span><svg width="12" height="12" viewBox="0 0 24 24" fill="none" stroke="#a9602c" stroke-width="2.5"><rect x="3" y="5" width="18" height="16"/><path d="M3 10h18M8 3v4M16 3v4"/></svg>30 March 2016</span><span><svg width="12" height="12" viewBox="0 0 24 24" fill="none" stroke="#a9602c" stroke-width="2.5"><path d="M4 4h16v12H8l-4 4z"/></svg>0 Comment</span></div>
        <p>Guests enjoyed an evening of design, dinner and a silent auction of studio pieces, with all proceeds going to partner charities in our community.</p>
        <div class="foot"><a class="btn">Learn More +</a></div>
      </div>
    </article>
    <div class="list">
      <div class="list-item"><div class="thumb t1" role="img" aria-label="Event photo"></div><div><h4>Studio news: new lighting line now in store</h4><div class="meta"><span>30 March 2016</span></div></div></div>
      <div class="list-item"><div class="thumb t2" role="img" aria-label="Event photo"></div><div><h4>Studio news: open house at the showroom</h4><div class="meta"><span>30 March 2016</span></div></div></div>
      <div class="list-item"><div class="thumb t3" role="img" aria-label="Event photo"></div><div><h4>Studio news: trade program now available</h4><div class="meta"><span>30 March 2016</span></div></div></div>
      <div class="list-item"><div class="thumb t4" role="img" aria-label="Event photo"></div><div><h4>Studio news: autumn charity gala dates set</h4><div class="meta"><span>30 March 2016</span></div></div></div>
    </div>
  </div>
</section>

<footer class="footer">
  <div class="wrap">
    <div>
      <div class="brand"><span class="brand-mark"></span><span class="brand-name">LORI VELL</span></div>
      <p class="about-text">As a child, Lori Vell spent weekends in her father's workshop, learning the craft of fine furniture.</p>
    </div>
    <div>
      <h5>Useful Links</h5>
      <ul><li>Home</li><li>About Us</li><li>Products</li><li>Blog</li><li>Event</li><li>News</li><li>Articles</li><li>Contact Us</li></ul>
    </div>
    <div>
      <h5>Contact Us</h5>
      <ul>
        <li><svg width="12" height="12" viewBox="0 0 24 24" fill="#c47a3f"><path d="M12 2a7 7 0 0 0-7 7c0 5 7 13 7 13s7-8 7-13a7 7 0 0 0-7-7zm0 9.5A2.5 2.5 0 1 1 12 6.5a2.5 2.5 0 0 1 0 5z"/></svg>418 Harlow Ave, Westbrook, CA</li>
        <li><svg width="12" height="12" viewBox="0 0 24 24" fill="#c47a3f"><path d="M6.6 10.8a15.1 15.1 0 0 0 6.6 6.6l2.2-2.2a1 1 0 0 1 1-.25 11.4 11.4 0 0 0 3.6.57 1 1 0 0 1 1 1V20a1 1 0 0 1-1 1A17 17 0 0 1 3 4a1 1 0 0 1 1-1h3.5a1 1 0 0 1 1 1c0 1.25.2 2.45.57 3.57a1 1 0 0 1-.25 1z"/></svg>040-555-0148</li>
        <li><svg width="12" height="12" viewBox="0 0 24 24" fill="#c47a3f"><path d="M3 5h18v14H3z"/></svg>323-555-0192</li>
        <li><svg width="12" height="12" viewBox="0 0 24 24" fill="none" stroke="#c47a3f" stroke-width="2.5"><rect x="3" y="5" width="18" height="14"/><path d="M3 6l9 7 9-7"/></svg>hello@lorivellstudio.com</li>
      </ul>
    </div>
    <div>
      <h5>Follow Us</h5>
      <ul><li><span class="dot"></span>Community</li><li><span class="dot"></span>Updates</li><li><span class="dot"></span>Network</li><li><span class="dot"></span>Gallery</li></ul>
    </div>
  </div>
</footer>
<div class="copyright">LORI VELL DESIGN - 2016 All Right Reserved</div>

</body>
</html>
```